Corroway Medical Imaging marketing poster

A poster to advertise our services. Something outstanding that catches the eye. Will be displayed at medical centres. Needs to advertise the following:
Opening hours - Mon-fri 8am-5:30pm Sat 8am-12:30
Services offered: Ultrasound, CT, Xray, Conebeam CT, Barium Studies, Injections and Biopsies, 3D/4D pregnancy scans.
We Bulk Bill concession card holders and under 18's
Locally owned and operated
www.corrowaymedicalimaging.example.au
include contact details also Tel: 96384027 Fax: 9638 4093

```html
<!DOCTYPE html>
<html lang="en">
<head>
<meta charset="utf-8">
<title>Corroway Medical Imaging – Poster Variants</title>
<link rel="stylesheet" href="https://fonts.googleapis.com/css2?family=Quicksand:wght@500;600;700&display=swap">
<style>
  :root{
    --page:#e9e7e3;
    --sky-deep:#0f9be3;
    --sky-light:#bfe9fb;
    --ink:#0d1a22;
    --night:#060708;
    --paper:#ffffff;
    --cyan:#2aa8e2;
    --lime:#a7c83b;
    --slate:#aab9c5;
    --slate-dark:#7a93a1;
    --charcoal:#17222a;
    --xray-light:#d3dce2;
    --xray-dark:#56656e;
  }
  *{box-sizing:border-box;margin:0;padding:0}
  html,body{width:1200px;height:638px;overflow:hidden}
  body{background:var(--page);font-family:"Quicksand",sans-serif;position:relative}
  .poster-row{position:absolute;left:20px;top:63px;display:flex;gap:40px}
  .poster{position:relative;width:360px;height:512px;overflow:hidden;background:var(--bg);color:var(--text)}
  .poster--blue{--bg:radial-gradient(ellipse at 50% 45%,var(--sky-light) 0%,#5cc6f3 45%,var(--sky-deep) 100%);--text:var(--ink);--head:#fff;--tag:var(--ink);--badge:var(--slate-dark);--badge-text:#fff;--box:var(--lime);--pill:transparent;--pill-text:var(--ink);--brand:#fff}
  .poster--night{--bg:var(--night);--text:#fff;--head:#fff;--tag:var(--cyan);--badge:var(--slate);--badge-text:var(--ink);--box:var(--slate);--pill:#5a5f63;--pill-text:#fff;--brand:#fff}
  .poster--paper{--bg:var(--paper);--text:var(--charcoal);--head:var(--charcoal);--tag:var(--cyan);--badge:var(--charcoal);--badge-text:#fff;--box:var(--slate);--pill:var(--charcoal);--pill-text:#fff;--brand:#3a8fc4}

  .brand{position:absolute;top:28px;left:0;right:0;display:flex;align-items:center;justify-content:center;gap:8px}
  .brand__dot{width:30px;height:30px;border-radius:50%;border:2px solid var(--brand)}
  .brand__name{font-weight:600;font-size:15px;line-height:17px;color:var(--brand);text-transform:uppercase;letter-spacing:.5px;max-width:140px}

  .headline{position:absolute;top:88px;left:0;right:0;text-align:center;font-weight:700;font-size:32px;line-height:30px;color:var(--head)}
  .tagline{position:absolute;top:151px;left:0;right:0;text-align:center;font-weight:700;font-size:12px;color:var(--tag)}

  .xray-arm{position:absolute;top:176px;left:28px;right:0;height:160px;border-radius:80px 0 0 80px;background:linear-gradient(90deg,var(--xray-light) 0%,#9aa8b1 40%,var(--xray-dark) 100%)}
  .badge{position:absolute;top:186px;right:54px;width:92px;height:92px;border-radius:50%;background:var(--badge);color:var(--badge-text);display:flex;align-items:center;justify-content:center;text-align:center;font-weight:700;font-size:13.5px;line-height:13px;padding:10px}

  .services{position:absolute;top:346px;left:10px;right:10px;text-align:center}
  .services__label{display:inline-block;background:var(--pill);color:var(--pill-text);font-weight:700;font-size:12px;padding:0 10px;border-radius:9px;line-height:16px}
  .services__list{margin-top:3px;font-weight:600;font-size:12.5px;line-height:15px}

  .info-boxes{position:absolute;top:405px;left:14px;right:14px;display:flex;gap:8px}
  .info-box{background:var(--box);color:var(--ink);border-radius:5px;height:48px;display:flex;align-items:center;justify-content:center;text-align:center;font-weight:600;font-size:10.5px;line-height:12px}
  .info-box--billing{flex:1.45}
  .info-box--hours{flex:1}

  .contact{position:absolute;top:466px;left:0;right:0;text-align:center;font-weight:700;font-size:12.5px;line-height:15px}
</style>
</head>
<body>
<main class="poster-row">
  <article class="poster poster--blue">
    <div class="brand"><span class="brand__dot"></span><span class="brand__name">Corroway Medical Imaging</span></div>
    <h1 class="headline">Why you go<br>anywhere else?</h1>
    <p class="tagline">Best Medical Imaging centre</p>
    <div class="xray-arm" role="img" aria-label="X-ray image of an arm giving a thumbs up"></div>
    <div class="badge">Your Medical Needs One Step Away</div>
    <section class="services">
      <h2 class="services__label">Services offered</h2>
      <p class="services__list">Ultrasound, CT, Xray, Conebeam CT, Barium Studies,<br>Injections and Biopsies, 3D/4D pregnancy scans.</p>
    </section>
    <div class="info-boxes">
      <p class="info-box info-box--billing">We Bulk Bill concession card holders<br>and under 18's<br>Locally owned and operated</p>
      <p class="info-box info-box--hours">Opening hours:<br>Mon-fri 8am-5:30pm<br>Sat 8am-12:30</p>
    </div>
    <p class="contact">www.corrowaymedicalimaging.example.au<br>Tel: 96384027 Fax: 9638 4093</p>
  </article>

  <article class="poster poster--night">
    <div class="brand"><span class="brand__dot"></span><span class="brand__name">Corroway Medical Imaging</span></div>
    <h1 class="headline">Why you go<br>anywhere else?</h1>
    <p class="tagline">Best Medical Imaging centre</p>
    <div class="xray-arm" role="img" aria-label="X-ray image of an arm giving a thumbs up"></div>
    <div class="badge">Your Medical Needs One Step Away</div>
    <section class="services">
      <h2 class="services__label">Services offered</h2>
      <p class="services__list">Ultrasound, CT, Xray, Conebeam CT, Barium Studies,<br>Injections and Biopsies, 3D/4D pregnancy scans.</p>
    </section>
    <div class="info-boxes">
      <p class="info-box info-box--billing">We Bulk Bill concession card holders<br>and under 18's<br>Locally owned and operated</p>
      <p class="info-box info-box--hours">Opening hours:<br>Mon-fri 8am-5:30pm<br>Sat 8am-12:30</p>
    </div>
    <p class="contact">www.corrowaymedicalimaging.example.au<br>Tel: 96384027 Fax: 9638 4093</p>
  </article>

  <article class="poster poster--paper">
    <div class="brand"><span class="brand__dot"></span><span class="brand__name">Corroway Medical Imaging</span></div>
    <h1 class="headline">Why you go<br>anywhere else?</h1>
    <p class="tagline">Best Medical Imaging centre</p>
    <div class="xray-arm" role="img" aria-label="X-ray image of an arm giving a thumbs up"></div>
    <div class="badge">Your Medical Needs One Step Away</div>
    <section class="services">
      <h2 class="services__label">Services offered</h2>
      <p class="services__list">Ultrasound, CT, Xray, Conebeam CT, Barium Studies,<br>Injections and Biopsies, 3D/4D pregnancy scans.</p>
    </section>
    <div class="info-boxes">
      <p class="info-box info-box--billing">We Bulk Bill concession card holders<br>and under 18's<br>Locally owned and operated</p>
      <p class="info-box info-box--hours">Opening hours:<br>Mon-fri 8am-5:30pm<br>Sat 8am-12:30</p>
    </div>
    <p class="contact">www.corrowaymedicalimaging.example.au<br>Tel: 96384027 Fax: 9638 4093</p>
  </article>
</main>
</body>
</html>
```